Quarlwick Builders Business Cards

I want to use the logo and make an unique business card that shows the textured Logo with brick and builings. I want to be able to stand out when I pass out business cards.

```html
<!DOCTYPE html>
<html lang="en">
<head>
<meta charset="utf-8">
<title>Quarlwick Builders Business Cards</title>
<link href="https://fonts.googleapis.com/css2?family=Montserrat:wght@400;500;700&display=swap" rel="stylesheet">
<style>
  :root{
    --stage:#2b2b2d;
    --card-dark:#050505;
    --card-light:#ffffff;
    --brick:#e8401c;
    --ink:#1c1c1c;
    --muted:#3a3a3a;
  }
  *{margin:0;padding:0;box-sizing:border-box}
  html,body{width:1200px;height:875px;overflow:hidden}
  body{background:var(--stage);font-family:"Montserrat",sans-serif;position:relative}
  .card{position:absolute;top:277px;width:560px;height:320px;border-radius:18px;overflow:hidden}
  .card-front{left:20px;background:var(--card-dark)}
  .card-back{left:620px;background:var(--card-light)}
  .brand{display:flex;align-items:center;gap:10px;font-weight:700;color:var(--brick);white-space:nowrap}
  .brand-mark{width:14px;height:14px;background:var(--brick)}
  .card-front .brand{position:absolute;left:50%;top:50%;transform:translate(-50%,-50%);font-size:34px}
  .card-back .brand{position:absolute;right:36px;top:40px;font-size:17px}
  .holder{position:absolute;left:40px;top:188px}
  .holder-name{font-weight:700;font-size:26px;color:var(--brick);line-height:1}
  .holder-title{font-weight:500;font-size:13px;color:var(--ink);margin-top:6px}
  .divider{position:absolute;left:40px;right:36px;top:236px;height:2px;background:var(--brick)}
  .contacts{position:absolute;left:40px;top:248px;list-style:none}
  .contacts li{display:flex;align-items:center;gap:10px;font-size:12.5px;color:var(--muted);height:20px}
  .contacts svg{width:13px;height:13px;fill:var(--brick)}
  .address{position:absolute;right:36px;top:248px;text-align:left;font-size:12.5px;line-height:1.45;color:var(--ink)}
</style>
</head>
<body>
  <section class="card card-front" aria-label="Card front">
    <div class="brand"><span class="brand-mark"></span>Quarlwick Builders</div>
  </section>

  <section class="card card-back" aria-label="Card back">
    <div class="brand"><span class="brand-mark"></span>Quarlwick Builders</div>
    <div class="holder">
      <p class="holder-name">Aldric Venn</p>
      <p class="holder-title">Managing Director</p>
    </div>
    <div class="divider"></div>
    <ul class="contacts">
      <li><svg viewBox="0 0 24 24"><path d="M6.6 10.8a15.1 15.1 0 0 0 6.6 6.6l2.2-2.2a1 1 0 0 1 1-.25 11.4 11.4 0 0 0 3.6.57 1 1 0 0 1 1 1V20a1 1 0 0 1-1 1A17 17 0 0 1 3 4a1 1 0 0 1 1-1h3.5a1 1 0 0 1 1 1c0 1.25.2 2.45.57 3.57a1 1 0 0 1-.25 1z"/></svg>(08) 4610 3382</li>
      <li><svg viewBox="0 0 24 24"><path d="M2 5h20v14H2z M2 5l10 8 10-8" /></svg>info@quarlwickbuild.com</li>
      <li><svg viewBox="0 0 24 24"><circle cx="12" cy="12" r="10"/></svg>www.quarlwickbuild.com</li>
    </ul>
    <p class="address">48 Ferrow Lane,<br>Aldmere, USA</p>
  </section>
</body>
</html>
```